Rolvexa

Hi everyone!

Looks like our project is more sophisticated than we expected. So good news - we increased the budget! and one of you will sure get the prize - no money back for us!

We are a young Russian company that specializes in in-taxi entertainment. We believe that our key strength is great attention to user experience. We've devoted much effort to improve ergonomics of our devices - tablet PCs that we install in the taxis. And yes, we enjoy to simplify things!

Now we need the most basic things - a logo and some staff for client meetings (primarily advertisers and ad agencies).

As for logo - we already have one engraved on the prototypes of our device (see attached file). This is one of the ideas (still far from perfect) - what we appreciate in it is minimalistic yet stylish approach.

As for "take it to the meeting stuff" we want to start with name card, pen and notepad (A4) that we will leave in clients's office, also as a reminder. Shall your have more smart ideas - always welcome!

As for logo and name cards - we would like to make an image of serious but modern company. Our design should communicate creativity and reliability. We believe that "to understand is to simplify" - minimalistic design is the most difficult one. Its better to work hard on fonts and arrangement, than put 10 variegated images.

SO THE TASK IS TO DESIGN:
- a logo
- a name card
- a note pad (great example in attachment)
- a pen

Shall you have more questions - please ask in comments.

We look forward to meeting like-minded fellows here!

Target Market(s)

Out target are:

- advertiser
- advertising agencies
- taxi passenger

Industry/Entity Type

It Company

Requirements
Must have
• font should be chosen very carefully
Nice to have
• classic minimalistic plain text only but very stylish name card is a dream of one of our co-founders:)
Should not have
• we do not want to have taxi-like colors and chess-boards. We are closer to "innovation", "entertainment", and "user experience", rather than "taxi".

```html
<!DOCTYPE html>
<html lang="en">
<head>
<meta charset="utf-8">
<title>Rolvexa — name card</title>
<link href="https://fonts.googleapis.com/css2?family=Alegreya+Sans:wght@300;400;700&display=swap" rel="stylesheet">
<style>
  :root {
    --ink: #4e7089;
    --ink-soft: #5f7f96;
    --rule: #b3bccb;
    --mist: #b0b9c6;
    --paper: #ffffff;
    --canvas: #ffffff;
  }
  * { margin: 0; padding: 0; box-sizing: border-box; }
  html, body {
    width: 1200px; height: 1000px; overflow: hidden;
    background: var(--canvas);
    font-family: "Alegreya Sans", sans-serif;
  }
  .name-card {
    position: absolute; left: 70px; top: 207px;
    width: 1063px; height: 590px;
    background: var(--paper);
    box-shadow: 0 2px 10px rgba(0,0,0,0.18);
  }
  .brand {
    position: absolute; left: 140px; top: 72px;
    font-size: 84px; font-weight: 300; line-height: 1;
    color: var(--ink); letter-spacing: 1px;
  }
  .identity {
    position: absolute; left: 270px; top: 263px;
    border-left: 3px solid var(--rule);
    padding-left: 17px;
    color: var(--ink);
  }
  .identity .person {
    font-size: 34px; font-weight: 700; line-height: 38px; letter-spacing: 2px;
  }
  .identity .role {
    font-size: 34px; font-weight: 400; line-height: 44px; letter-spacing: 2.5px;
    color: var(--ink-soft);
  }
  .contact {
    position: absolute; right: 111px; top: 480px;
    text-align: right; color: var(--ink);
    font-size: 27px; font-weight: 400; line-height: 35px; letter-spacing: 2.6px;
  }
  .web-rule {
    position: absolute; left: 975px; top: 148px;
    width: 3px; height: 395px; background: var(--rule);
  }
  .web-vertical {
    position: absolute; left: 993px; top: 140px; width: 28px;
    list-style: none; text-align: center;
    font-size: 25px; font-weight: 300; line-height: 26.7px;
  }
  .web-vertical .muted { color: var(--mist); }
  .web-vertical .strong { color: var(--ink); font-weight: 400; }
</style>
</head>
<body>
  <section class="name-card">
    <div class="brand">rolvexa</div>

    <div class="identity">
      <p class="person">Name</p>
      <p class="person">Lastname</p>
      <p class="role">position</p>
    </div>

    <div class="contact">
      <p class="phone">+7 55548219</p>
      <p class="email">hello@rolvexa.com</p>
    </div>

    <div class="web-rule"></div>
    <ul class="web-vertical" aria-label="www.rolvexa.com">
      <li class="muted">w</li>
      <li class="muted">w</li>
      <li class="muted">w</li>
      <li class="muted">.</li>
      <li class="strong">r</li>
      <li class="strong">o</li>
      <li class="strong">l</li>
      <li class="strong">v</li>
      <li class="strong">e</li>
      <li class="strong">x</li>
      <li class="strong">a</li>
      <li class="muted">.</li>
      <li class="muted">c</li>
      <li class="muted">o</li>
      <li class="muted">m</li>
    </ul>
  </section>
</body>
</html>
```